Construction Company Website

I need a website for my construction company
Target Market(s)
People looking for construction work
Coding
Coded - Design and coding required
Number of Pages Required
4 page
Colors
0455a3
ffc214
Requirements
Must have
- A home page about my company,
A completed projects page showcasing some completed works
A contact me page with an enquiry form
Nice to have
- Professional and contemporary whilst classy website.

```html
<!DOCTYPE html>
<html lang="en">
<head>
<meta charset="utf-8">
<title>Halden Construction</title>
<link href="https://fonts.googleapis.com/css2?family=Poppins:wght@400;500;600;700&display=swap" rel="stylesheet">
<style>
:root{
  --navy:#17243d;
  --blue:#0455a3;
  --yellow:#ffc214;
  --ink:#1d1d1d;
  --body:#3b3b3b;
  --muted:#777;
  --paper:#f5f4f4;
  --line:#c9c9c9;
}
*{box-sizing:border-box;margin:0;padding:0}
html,body{width:1200px;height:4292px;overflow:hidden}
body{position:relative;font-family:'Poppins',sans-serif;color:var(--ink);background:#fff}
.abs{position:absolute}
.center{left:0;width:1200px;text-align:center}

/* header */
.site-header{left:0;top:0;width:1200px;height:112px;background:var(--navy);z-index:5}
.brand-plate{left:58px;top:0;width:334px;height:170px;background:var(--navy);border-radius:0 0 40px 40px;z-index:6;display:flex;flex-direction:column;align-items:center;justify-content:center;gap:14px;padding-top:10px}
.brand-square{width:46px;height:46px;background:var(--yellow)}
.brand-name{color:var(--yellow);font-weight:500;font-size:18px;letter-spacing:3px;white-space:nowrap}
.nav{top:46px;left:552px;display:flex;gap:38px;font-size:14px;font-weight:500;color:#fff;z-index:6}
.nav .active{color:var(--yellow);position:relative}
.nav .active::before{content:"";position:absolute;left:50%;top:-12px;width:8px;height:8px;margin-left:-4px;border-radius:50%;background:var(--yellow)}
.btn-contact{left:980px;top:38px;width:125px;height:40px;background:var(--yellow);color:#fff;font-size:14px;font-weight:600;display:flex;align-items:center;justify-content:center;z-index:6}

/* hero */
.hero-photo{left:0;top:112px;width:1200px;height:670px;background:linear-gradient(180deg,#8aa4b8 0%,#c9b89a 30%,#a8704f 60%,#7a4a30 100%)}
.hero-title{top:410px;font-size:54px;font-weight:700;color:#fff;text-shadow:0 2px 8px rgba(0,0,0,.35)}
.hero-sub{top:478px;font-size:43px;font-weight:700;color:#fff;text-shadow:0 2px 8px rgba(0,0,0,.35)}
.hero-sub .bar{display:inline-block;width:2px;height:38px;background:rgba(255,255,255,.7);margin:0 18px;vertical-align:-4px}
.btn-blue{background:var(--blue);color:#fff;font-size:16px;font-weight:600;display:flex;align-items:center;justify-content:center;border-radius:3px}
.hero-btn{left:513px;top:560px;width:172px;height:52px}
.arrow{width:50px;height:50px;border-radius:50%;border:2px solid #fff;display:flex;align-items:center;justify-content:center}
.arrow.gold{background:var(--yellow);border-color:var(--yellow)}
.arrow.grey{border-color:#888}

/* about */
.about-bg{left:0;top:700px;width:1200px;height:680px}
.about-title{top:875px;font-size:56px;font-weight:700;letter-spacing:-1px}
.about-kicker{top:945px;font-size:38px;font-weight:500;color:var(--yellow)}
.about-text{left:265px;width:670px;font-size:16px;line-height:30px;color:var(--body);text-align:center}
.about-btn{left:513px;top:1220px;width:172px;height:52px}

/* tiles */
.tile{top:1375px;height:373px;color:#fff;font-size:22px;font-weight:600;text-align:center}
.tile .label{position:absolute;left:0;right:0;top:252px}
.tile .chev{position:absolute;left:50%;top:300px;margin-left:-17px;width:34px;height:34px;border:2px solid #fff;border-radius:50%;display:flex;align-items:center;justify-content:center}

/* service cards */
.svc{background:#fff;border:2px solid #d8d8d8;text-align:center;padding-top:30px}
.svc h3{font-size:18px;font-weight:600;line-height:24px;margin-top:20px}
.svc p{font-size:14px;line-height:21px;color:var(--body);margin-top:12px}
.svc.feature{background:var(--yellow);border:none;color:#fff;box-shadow:0 10px 24px rgba(0,0,0,.18)}
.svc.feature p{color:#fff}

/* projects */
.projects-title{top:2385px;font-size:44px;font-weight:600;color:#fff}
.projects-title span,.accent{color:var(--yellow)}
.proj{top:2485px;width:264px;height:270px}

/* testimonials */
.t-title{top:2988px;font-size:38px;font-weight:600}
.quote{top:3072px;width:275px;height:186px;background:#fff;box-shadow:0 4px 18px rgba(0,0,0,.1);text-align:center;padding:20px 28px}
.quote::after{content:"";position:absolute;left:50%;bottom:-10px;margin-left:-10px;border:10px solid transparent;border-bottom:0;border-top-color:#fff}
.stars{color:var(--yellow);font-size:17px;letter-spacing:2px}
.quote h4{font-size:13px;font-weight:500;margin-top:6px}
.quote p{font-size:11px;line-height:20px;color:var(--muted);margin-top:8px}
.avatar{top:3283px;width:60px;height:60px;border-radius:50%;background:linear-gradient(#c8ccd2,#8d949c)}
.person{top:3350px;width:275px;text-align:center;font-size:12px;line-height:20px}
.person b{font-weight:600}
.dots{top:3414px;left:567px;display:flex;gap:7px}
.dots i{width:10px;height:10px;border-radius:50%;border:1px solid #999}
.dots i.on{background:#ff5a1f;border-color:#ff5a1f}

/* contact */
.contact-bg{left:0;top:3478px;width:1200px;height:480px;background:var(--paper)}
.contact-title{top:3523px;font-size:56px;font-weight:700}
.field{border:2px solid var(--line);background:var(--paper);font-size:17px;color:#555;padding:10px 18px}
.btn-outline{left:517px;top:3848px;width:166px;height:49px;border:2px solid var(--blue);border-radius:26px;color:var(--blue);font-size:16px;font-weight:600;display:flex;align-items:center;justify-content:center}

/* footer */
.footer{left:0;top:3958px;width:1200px;height:334px;background:var(--navy);color:#fff}
.foot-brand{left:100px;top:4040px;width:340px;display:flex;flex-direction:column;align-items:center;gap:18px}
.foot-brand .brand-square{width:70px;height:70px}
.foot-brand .brand-name{font-size:20px;letter-spacing:3px}
.foot-h{top:4020px;font-size:20px;font-weight:600;color:var(--yellow)}
.foot-list{font-size:14px;line-height:27px;color:#e6e6e6;list-style:none}
.foot-contact{left:485px;top:4058px;font-size:14px;line-height:18px;color:#e6e6e6}
.foot-contact div{display:flex;gap:10px;align-items:flex-start;margin-bottom:18px}
.foot-rule{left:0;top:4222px;width:1200px;height:1px;background:rgba(255,255,255,.25)}
.copy{top:4242px;font-size:13px;color:#ddd}
</style>
</head>
<body>

<header>
  <div class="abs site-header"></div>
  <div class="abs brand-plate"><span class="brand-square"></span><span class="brand-name">HALDEN CONSTRUCTION</span></div>
  <nav class="abs nav"><span class="active">HOME</span><span>ABOUT US</span><span>PROJECTS</span><span>SERVICES</span></nav>
  <div class="abs btn-contact">CONTACT</div>
</header>

<section class="hero">
  <div class="abs hero-photo" role="img" aria-label="Construction site with laid timber formwork and building materials at sunset"></div>
  <div class="abs center hero-title">Groundworks</div>
  <div class="abs center hero-sub">Landscaping<span class="bar"></span>Extensions</div>
  <div class="abs btn-blue hero-btn">FREE ESTIMATES</div>
  <div class="abs arrow" style="left:105px;top:392px"><svg width="18" height="18" viewBox="0 0 18 18"><path d="M12 2 5 9l7 7" fill="none" stroke="#fff" stroke-width="2"/></svg></div>
  <div class="abs arrow gold" style="left:1042px;top:392px"><svg width="18" height="18" viewBox="0 0 18 18"><path d="M6 2l7 7-7 7" fill="none" stroke="#fff" stroke-width="2"/></svg></div>
</section>

<section class="about">
  <div class="abs about-bg" role="img" aria-label="Soft sky with clouds over misty hills and a green meadow" style="background:linear-gradient(180deg,#cfe6f6 0%,#eaf3f9 45%,#e3ecee 70%,#d6e2bf 100%)"></div>
  <svg class="abs" style="left:0;top:690px" width="1200" height="95" viewBox="0 0 1200 95">
    <path d="M0 10 L600 85 L1200 10 L1200 0 L0 0Z" fill="#7a4a30"/>
    <path d="M0 10 L600 85 L1200 10" fill="none" stroke="var(--yellow)" stroke-width="6"/>
  </svg>
  <h1 class="abs center about-title">ABOUT</h1>
  <h2 class="abs center about-kicker">CONSTRUCTION</h2>
  <p class="abs about-text" style="top:1013px">Lorem Ipsum is simply dummy text of the printing and typesetting industry. Lorem Ipsum has been the industry's standard dummy text ever since the 1500s, when an unknown printer took a galley of type and scrambled it to make.</p>
  <p class="abs about-text" style="top:1127px">Lorem Ipsum is simply dummy text of the printing and typesetting industry. Lorem Ipsum has been the industry's standard dummy text ever since</p>
  <div class="abs btn-blue about-btn">FREE ESTIMATES</div>
</section>

<section class="tiles">
  <div class="abs tile" style="left:0;width:392px;background:linear-gradient(180deg,#5b6b4a,#3fa0c8 40%,#6b4a36 75%,#4a3426)" role="img" aria-label="Newly installed swimming pool with paving">
    <div class="label">GROUNDWORKS</div><div class="chev"><svg width="14" height="10" viewBox="0 0 14 10"><path d="M1 2l6 6 6-6" fill="none" stroke="#fff" stroke-width="2"/></svg></div></div>
  <div class="abs tile" style="left:400px;width:400px;background:linear-gradient(160deg,#3c6a2a,#9a4a2a 45%,#a2502e 60%,#4e8a2c)" role="img" aria-label="Brick garden path through green lawn and shrubs">
    <div class="label">LANDSCAPING</div><div class="chev"><svg width="14" height="10" viewBox="0 0 14 10"><path d="M1 2l6 6 6-6" fill="none" stroke="#fff" stroke-width="2"/></svg></div></div>
  <div class="abs tile" style="left:808px;width:392px;background:linear-gradient(180deg,#5a6e8a,#4f7a3a 40%,#6b7a52 70%,#c8bfa8)" role="img" aria-label="House extension with ivy-covered wall">
    <div class="label">EXTENSIONS</div><div class="chev"><svg width="14" height="10" viewBox="0 0 14 10"><path d="M1 2l6 6 6-6" fill="none" stroke="#fff" stroke-width="2"/></svg></div></div>
</section>

<section class="services">
  <div class="abs arrow grey" style="left:108px;top:1967px"><svg width="18" height="18" viewBox="0 0 18 18"><path d="M12 2 5 9l7 7" fill="none" stroke="#888" stroke-width="2"/></svg></div>
  <div class="abs arrow grey" style="left:1042px;top:1967px"><svg width="18" height="18" viewBox="0 0 18 18"><path d="M6 2l7 7-7 7" fill="none" stroke="#888" stroke-width="2"/></svg></div>
  <div class="abs svc" style="left:185px;top:1862px;width:255px;height:266px">
    <svg width="66" height="66" viewBox="0 0 66 66"><g fill="none" stroke="var(--blue)" stroke-width="2"><rect x="6" y="6" width="54" height="30"/><path d="M6 16h54M6 26h54M18 6v10M30 6v10M42 6v10M24 16v10M36 16v10M48 16v10M12 26v10M30 26v10M48 26v10M14 44l20 16 10-8-20-16z"/></g></svg>
    <h3>GROUND<br>CONCRETE WORK</h3><p>Lorem Ipsum is simply<br>dummy text of the printing</p></div>
  <div class="abs svc feature" style="left:472px;top:1885px;width:256px;height:268px">
    <svg width="66" height="66" viewBox="0 0 66 66"><g fill="none" stroke="#fff" stroke-width="2"><path d="M4 60h58M8 60V30h20v30M12 30c0-10 12-10 12 0M30 60c10-20 20-24 32-24M38 60c6-10 14-14 24-14"/><circle cx="46" cy="14" r="6"/></g></svg>
    <h3>SOFT<br>LANDSCAPING</h3><p>Lorem Ipsum is simply<br>dummy text of the printing</p></div>
  <div class="abs svc" style="left:760px;top:1862px;width:255px;height:266px">
    <svg width="66" height="66" viewBox="0 0 66 66"><g fill="none" stroke="var(--blue)" stroke-width="2"><path d="M4 60h58V30H4z M4 44l58-10M14 60l8-28M30 60l4-30M46 60l0-28"/><circle cx="40" cy="12" r="6"/></g></svg>
    <h3>HARD<br>LANDSCAPING</h3><p>Lorem Ipsum is simply<br>dummy text of the printing</p></div>
</section>

<section class="projects">
  <svg class="abs" style="left:0;top:2278px" width="1200" height="632" viewBox="0 0 1200 632">
    <path d="M0 85 L600 5 L1200 85 V632 H0Z" fill="var(--navy)"/>
    <path d="M0 85 L600 5 L1200 85" fill="none" stroke="var(--yellow)" stroke-width="6"/>
  </svg>
  <h2 class="abs center projects-title">COMPLETED <span>PROJECTS</span></h2>
  <div class="abs arrow" style="left:82px;top:2585px"><svg width="18" height="18" viewBox="0 0 18 18"><path d="M12 2 5 9l7 7" fill="none" stroke="#fff" stroke-width="2"/></svg></div>
  <div class="abs arrow" style="left:1067px;top:2585px"><svg width="18" height="18" viewBox="0 0 18 18"><path d="M6 2l7 7-7 7" fill="none" stroke="#fff" stroke-width="2"/></svg></div>
  <svg class="abs proj" style="left:157px" viewBox="0 0 264 270" role="img" aria-label="Garden with new artificial lawn and timber edging"><defs><linearGradient id="g1" x1="0" y1="0" x2="0" y2="1"><stop offset="0" stop-color="#8a6a4a"/><stop offset=".45" stop-color="#4fae3a"/><stop offset="1" stop-color="#c9a46a"/></linearGradient></defs><path d="M0 0H264V270L0 250Z" fill="url(#g1)"/><path d="M0 250 264 270" stroke="var(--yellow)" stroke-width="6"/></svg>
  <svg class="abs proj" style="left:468px" viewBox="0 0 264 270" role="img" aria-label="Red brick house with new conservatory"><defs><linearGradient id="g2" x1="0" y1="0" x2="0" y2="1"><stop offset="0" stop-color="#a03a2a"/><stop offset=".55" stop-color="#d8d8d4"/><stop offset="1" stop-color="#7a8a4a"/></linearGradient></defs><path d="M0 0H264V270L0 250Z" fill="url(#g2)"/><path d="M0 250 264 270" stroke="var(--yellow)" stroke-width="6"/></svg>
  <svg class="abs proj" style="left:780px" viewBox="0 0 264 270" role="img" aria-label="Swimming pool with stone paving surround"><defs><linearGradient id="g3" x1="0" y1="0" x2="0" y2="1"><stop offset="0" stop-color="#4a6a3a"/><stop offset=".4" stop-color="#3fa6d0"/><stop offset=".7" stop-color="#9a6a4a"/><stop offset="1" stop-color="#a8a8a4"/></linearGradient></defs><path d="M0 0H264V270L0 250Z" fill="url(#g3)"/><path d="M0 250 264 270" stroke="var(--yellow)" stroke-width="6"/></svg>
</section>

<section class="testimonials">
  <h2 class="abs center t-title">CLIENT <span class="accent">TESTIMONIALS</span></h2>
  <div class="abs quote" style="left:162px"><div class="stars">★★★★★</div><h4>"SOLID Service! Vety consistent!"</h4><p>the printing and typesetting industry. Lorem Ipsum has been the industry's standard dummy text ever since the 1500s Lorem Ipsum!</p></div>
  <div class="abs quote" style="left:462px"><div class="stars">★★★★★</div><h4>"SOLID Service! Vety consistent!"</h4><p>the printing and typesetting industry. Lorem Ipsum has been the industry's standard dummy text ever since the 1500s Lorem Ipsum!</p></div>
  <div class="abs quote" style="left:762px"><div class="stars">★★★★★</div><h4>"SOLID Service! Vety consistent!"</h4><p>the printing and typesetting industry. Lorem Ipsum has been the industry's standard dummy text ever since the 1500s Lorem Ipsum!</p></div>
  <div class="abs avatar" style="left:270px" role="img" aria-label="Client portrait"></div>
  <div class="abs avatar" style="left:570px" role="img" aria-label="Client portrait"></div>
  <div class="abs avatar" style="left:870px" role="img" aria-label="Client portrait"></div>
  <div class="abs person" style="left:162px"><b>Marla Greene</b><br>Web Development</div>
  <div class="abs person" style="left:462px"><b>Marla Greene</b><br>Web Development</div>
  <div class="abs person" style="left:762px"><b>Marla Greene</b><br>Web Development</div>
  <div class="abs dots"><i></i><i class="on"></i><i></i><i></i></div>
</section>

<section class="contact">
  <div class="abs contact-bg"></div>
  <h2 class="abs center contact-title">GET IN <span class="accent">TOUCH</span></h2>
  <div class="abs field" style="left:273px;top:3622px;width:314px;height:46px">Your Name</div>
  <div class="abs field" style="left:613px;top:3622px;width:312px;height:46px">Subject</div>
  <div class="abs field" style="left:273px;top:3693px;width:314px;height:46px">Email Address</div>
  <div class="abs field" style="left:613px;top:3693px;width:312px;height:119px"></div>
  <div class="abs field" style="left:273px;top:3765px;width:314px;height:46px">Phone</div>
  <div class="abs btn-outline">LEARN MORE</div>
</section>

<footer>
  <div class="abs footer"></div>
  <div class="abs foot-brand"><span class="brand-square"></span><span class="brand-name">HALDEN CONSTRUCTION</span></div>
  <div class="abs foot-h" style="left:485px">CONTACT US</div>
  <div class="abs foot-contact">
    <div><svg width="12" height="16" viewBox="0 0 12 16"><path d="M6 0a6 6 0 0 1 6 6c0 4-6 10-6 10S0 10 0 6a6 6 0 0 1 6-6z" fill="#fff"/><circle cx="6" cy="6" r="2.2" fill="var(--navy)"/></svg><span>42 Elmstead Road, Suite 7<br>Avon 20418</span></div>
    <div><svg width="14" height="14" viewBox="0 0 14 14"><path d="M3 0l3 3-2 2c1 2 3 4 5 5l2-2 3 3-2 3C6 14 0 8 0 3z" fill="#fff"/></svg><span>(555) 014 2260</span></div>
    <div><svg width="16" height="12" viewBox="0 0 16 12"><rect width="16" height="12" fill="#fff"/><path d="M0 0l8 7 8-7" fill="none" stroke="var(--navy)" stroke-width="1.5"/></svg><span>hello@haldenbuild.com</span></div>
  </div>
  <div class="abs foot-h" style="left:778px">COMPANY</div>
  <ul class="abs foot-list" style="left:778px;top:4050px"><li>Home</li><li>About Us</li><li>Projects</li><li>Services</li></ul>
  <div class="abs foot-h" style="left:957px">RESOURCES</div>
  <ul class="abs foot-list" style="left:957px;top:4050px"><li>Testimonials</li><li>Sitemap</li><li>Cotact Us</li><li>Support</li></ul>
  <div class="abs foot-rule"></div>
  <div class="abs center copy">© 2020 Halden Construction. All Rights are Reserved.</div>
</footer>

</body>
</html>
```